Business Card Designs

Looking to design a 3.5" x 2" standard business card for our employees.
The design needs to be sleek, simple, and modern. We would like our logo (attached) to be incorporated, but not in that colour, rather an outline of the logo in either gold or silver (whichever looks better).

Modern and Simple is what we are looking for, but be creative in incorporating the logo.

```html
<!DOCTYPE html>
<html lang="en">
<head>
<meta charset="utf-8">
<title>Harbourline Suites – Business Card</title>
<link href="https://fonts.googleapis.com/css2?family=Raleway:wght@400;600;800&family=Roboto+Condensed:wght@400&display=swap" rel="stylesheet">
<style>
  :root {
    --backdrop: #d7d7d7;
    --teal: #5fabab;
    --paper: #ffffff;
    --ink-light: #ffffff;
  }
  * { box-sizing: border-box; margin: 0; padding: 0; }
  html, body {
    width: 1200px; height: 846px; overflow: hidden;
    background: var(--backdrop);
  }
  .canvas { position: relative; width: 1200px; height: 846px; }
  .card {
    position: absolute; width: 540px; height: 309px;
    box-shadow: 0 6px 18px rgba(0,0,0,0.12);
    overflow: hidden;
  }
  .card--front { left: 50px; top: 150px; background: var(--paper); }
  .card--back  { left: 610px; top: 390px; background: var(--teal); }

  .brand {
    position: absolute; display: flex; align-items: center; gap: 10px;
    font-family: "Raleway", sans-serif; font-weight: 600;
    letter-spacing: 0.12em; text-transform: uppercase;
  }
  .brand__mark { width: 14px; height: 14px; flex: none; }
  .brand__name { line-height: 1.2; }
  .card--front .brand { left: 34px; top: 104px; width: 190px; color: var(--teal); font-size: 16px; }
  .card--front .brand__name { display: flex; flex-direction: column; }
  .card--front .brand__mark { background: var(--teal); }
  .card--back .brand { left: 0; right: 0; top: 110px; justify-content: center; color: var(--ink-light); font-size: 26px; }
  .card--back .brand__mark { background: var(--ink-light); width: 18px; height: 18px; }

  .contact {
    position: absolute; left: 250px; top: 36px; right: 20px; color: var(--teal);
    font-family: "Raleway", sans-serif;
  }
  .contact__name { font-weight: 800; font-size: 22px; margin-bottom: 12px; }
  .contact__list { list-style: none; font-size: 12.5px; line-height: 1.35; }
  .contact__item { display: flex; align-items: flex-start; gap: 8px; margin-bottom: 3px; }
  .contact__icon { width: 13px; height: 13px; flex: none; margin-top: 2px; }

  .band {
    position: absolute; left: 0; right: 0; top: 238px; height: 20px;
    background: var(--teal);
  }

  .tagline {
    position: absolute; left: 0; right: 0; bottom: 34px; text-align: center;
    color: var(--ink-light); font-family: "Roboto Condensed", sans-serif;
    font-size: 15px; text-transform: uppercase; letter-spacing: 0.01em;
  }
</style>
</head>
<body>
<main class="canvas">
  <section class="card card--front">
    <div class="brand"><span class="brand__mark"></span><span class="brand__name"><span>Harbourline</span><span>Suites</span></span></div>

    <div class="contact">
      <p class="contact__name">Name Lastname</p>
      <ul class="contact__list">
        <li class="contact__item">
          <svg class="contact__icon" viewBox="0 0 16 16"><path d="M4 1.5l2.2 3-1.4 1.6a8 8 0 0 0 5.1 5.1l1.6-1.4 3 2.2-1.2 2.4C7 14.5 1.5 9 1.6 2.7z" fill="currentColor"/></svg>
          <span>Local: 555-014-2280</span>
        </li>
        <li class="contact__item">
          <svg class="contact__icon" viewBox="0 0 16 16"><path d="M4 1.5l2.2 3-1.4 1.6a8 8 0 0 0 5.1 5.1l1.6-1.4 3 2.2-1.2 2.4C7 14.5 1.5 9 1.6 2.7z" fill="currentColor"/></svg>
          <span>TOLL FREE: (555) 010-4471</span>
        </li>
        <li class="contact__item">
          <svg class="contact__icon" viewBox="0 0 16 16"><rect x="1" y="3" width="14" height="10" fill="currentColor"/><path d="M1 3l7 6 7-6" fill="none" stroke="#fff" stroke-width="1.2"/></svg>
          <span>info@harbourlinesuites.com</span>
        </li>
        <li class="contact__item">
          <svg class="contact__icon" viewBox="0 0 16 16" fill="none" stroke="currentColor" stroke-width="1.2"><circle cx="8" cy="8" r="6.5"/><ellipse cx="8" cy="8" rx="3" ry="6.5"/><path d="M1.5 8h13"/></svg>
          <span>www.harbourlinesuites.com</span>
        </li>
        <li class="contact__item">
          <svg class="contact__icon" viewBox="0 0 16 16"><path d="M8 1a5 5 0 0 1 5 5c0 4-5 9-5 9S3 10 3 6a5 5 0 0 1 5-5z" fill="currentColor"/><circle cx="8" cy="6" r="1.8" fill="#fff"/></svg>
          <span>12 Lakeview Ave, Suite 300 Riverton,<br>ON A1B 2C3</span>
        </li>
      </ul>
    </div>

    <div class="band"></div>
  </section>

  <section class="card card--back">
    <div class="brand"><span class="brand__mark"></span><span class="brand__name">Harbourline Suites</span></div>
    <p class="tagline">We provide the best designed short term rentals Riverton has to offer.</p>
  </section>
</main>
</body>
</html>
```